Design a double sided business card

We are looking for a clean, eye-catching, and contemporary design that enhances the brand and presents a premium, professional image. Our preference is for a brown card with black gloss detailing and embossed elements; however, we are open to creative input and design suggestions that best achieve a strong visual impact.

Please see the attached existing business card for reference. We use both black and brown colours consistently across our branding.

On sample provided

```html
<!DOCTYPE html>
<html lang="en">
<head>
<meta charset="utf-8">
<title>Halden – Business Card</title>
<link rel="stylesheet" href="https://fonts.googleapis.com/css2?family=Montserrat:wght@700;800&family=Roboto:wght@400&display=swap">
<style>
  :root {
    --backdrop: #5a5a5a;
    --card-dark: #2e2e2e;
    --brand-tan: #c9b59c;
    --ink: #111111;
    --paper: #ffffff;
    --text-light: #f2f2f2;
  }
  * { box-sizing: border-box; margin: 0; padding: 0; }
  html, body { width: 1200px; height: 1200px; overflow: hidden; }
  body { background: var(--backdrop); position: relative; font-family: "Roboto", Arial, sans-serif; }

  .card { position: absolute; width: 690px; height: 394px; overflow: hidden; }
  .card--front { left: 267px; top: 158px; background: var(--card-dark); }
  .card--back { left: 260px; top: 651px; background: var(--brand-tan); }

  .brand-name {
    position: absolute;
    font-family: "Montserrat", Arial, sans-serif;
    font-weight: 800;
    letter-spacing: 0.14em;
    white-space: nowrap;
    transform: translateX(-50%);
  }
  .card--front .brand-name { left: 218px; top: 140px; font-size: 38px; color: var(--brand-tan); }
  .card--back .brand-name { left: 50%; top: 165px; font-size: 54px; color: var(--ink); }

  .divider { position: absolute; left: 360px; top: 68px; width: 2px; height: 196px; background: #4a4a4a; }

  .contact { position: absolute; left: 391px; top: 74px; color: var(--text-light); }
  .contact__name {
    font-family: "Montserrat", Arial, sans-serif; font-weight: 800;
    font-size: 25px; letter-spacing: -0.01em; color: var(--brand-tan); line-height: 1;
  }
  .contact__role { font-size: 15px; margin-top: 6px; }
  .contact__address { font-size: 16px; line-height: 21px; margin-top: 21px; }
  .contact__list { list-style: none; margin-top: 12px; font-size: 16px; }
  .contact__list li { display: flex; align-items: center; height: 20.5px; }
  .contact__list svg { width: 13px; height: 13px; margin-right: 12px; flex: none; }

  .web-band { position: absolute; left: 0; top: 324px; width: 100%; height: 35px; display: flex; }
  .web-band__tan { width: 539px; background: var(--brand-tan); position: relative; }
  .web-band__url {
    position: absolute; left: 121px; top: 8px; font-size: 15px;
    letter-spacing: 0.16em; color: var(--ink);
  }
  .web-band__mark { width: 42px; background: var(--brand-tan); display: flex; align-items: center; justify-content: center; }
  .web-band__mark span { width: 26px; height: 26px; background: var(--card-dark); display: block; }
  .web-band__white { flex: 1; background: var(--paper); }
</style>
</head>
<body>

<section class="card card--front" aria-label="Card front">
  <div class="brand-name">HALDEN</div>
  <div class="divider"></div>

  <div class="contact">
    <div class="contact__name">DEV KALRA</div>
    <div class="contact__role">Director</div>
    <div class="contact__address">The Old Mill Yard<br>Eastbridge EB4 2LN</div>
    <ul class="contact__list">
      <li>
        <svg viewBox="0 0 24 24" aria-hidden="true"><path fill="#c9b59c" d="M6.6 10.8a15.1 15.1 0 0 0 6.6 6.6l2.2-2.2c.3-.3.7-.4 1-.2 1.1.4 2.3.6 3.6.6.6 0 1 .4 1 1V20c0 .6-.4 1-1 1C10.6 21 3 13.4 3 4c0-.6.4-1 1-1h3.5c.6 0 1 .4 1 1 0 1.3.2 2.5.6 3.6.1.3 0 .7-.2 1z"/></svg>
        0800 555 0142
      </li>
      <li>
        <svg viewBox="0 0 24 24" aria-hidden="true"><rect x="6" y="1.5" width="12" height="21" rx="2" fill="none" stroke="#f2f2f2" stroke-width="2"/><line x1="10" y1="19" x2="14" y2="19" stroke="#f2f2f2" stroke-width="1.6"/></svg>
        07700900456
      </li>
      <li>
        <svg viewBox="0 0 24 24" aria-hidden="true"><rect x="2" y="5" width="20" height="14" fill="#c9b59c"/><path d="M2 5l10 8 10-8" fill="none" stroke="#2e2e2e" stroke-width="1.6"/></svg>
        dev@halden.co.uk
      </li>
    </ul>
  </div>

  <div class="web-band">
    <div class="web-band__tan"><span class="web-band__url">www.halden.co.uk</span></div>
    <div class="web-band__mark"><span></span></div>
    <div class="web-band__white"></div>
  </div>
</section>

<section class="card card--back" aria-label="Card back">
  <div class="brand-name">HALDEN</div>
</section>

</body>
</html>
```